Promotional brochure for educational consulting firm

Hi Designers!

Please do a 8.5 x 11 inch tri-fold brochure as well as a 8.5 x 11 inch half-fold brochure.  I appreciate black and white versions in addition to color.  Please take a look at my company's website for a better sense of the look and feel I am going for:  www.brightlarkedu.org

Thanks!

Industry/Entity Type

Consulting

Colors
3176b5
85abd2
fcfbfd

```html
<!DOCTYPE html>
<html lang="en">
<head>
<meta charset="utf-8">
<title>Brightlark Associates – Tri-fold Brochure</title>
<link href="https://fonts.googleapis.com/css2?family=Montserrat:wght@500;600;700&family=Mulish:wght@400;600;700&display=swap" rel="stylesheet">
<style>
  :root {
    --blue-deep: #1d4f80;
    --blue: #3176b5;
    --blue-light: #85abd2;
    --paper: #fcfbfd;
    --backdrop: #e6e8eb;
    --ink-dark: #13283d;
  }
  * { box-sizing: border-box; margin: 0; padding: 0; }
  html, body { width: 1200px; height: 1000px; overflow: hidden; background: var(--backdrop); }
  body { font-family: "Mulish", sans-serif; }

  .canvas { position: relative; width: 1200px; height: 1000px; overflow: hidden; }
  .brochure {
    position: absolute; left: 60px; top: 83px;
    width: 1080px; height: 834px;
    display: flex; box-shadow: 0 6px 24px rgba(0,0,0,.18);
  }
  .panel { position: relative; width: 360px; height: 834px; overflow: hidden; background: var(--paper); }
  .panel + .panel { border-left: 1px solid rgba(0,0,0,.06); }

  .photo { position: absolute; left: 0; width: 100%; }
  .shape { position: absolute; left: 0; width: 100%; display: block; }

  .brand { position: absolute; left: 0; width: 100%; text-align: center; }
  .brand-mark {
    display: inline-block; width: 44px; height: 44px; border-radius: 50%;
    background: var(--blue); margin-bottom: 10px;
  }
  .brand-name {
    font-family: "Montserrat", sans-serif; font-weight: 600;
    font-size: 19px; letter-spacing: .5px; color: var(--blue);
  }
  .brand-tagline {
    font-size: 10px; letter-spacing: 1px; text-transform: uppercase;
    color: var(--blue); margin-top: 3px;
  }

  .motto-tab {
    position: absolute; color: #fff; background: var(--blue);
    font-size: 11px; font-weight: 600; padding: 6px 18px;
    white-space: nowrap;
  }

  h2.section-title {
    font-family: "Montserrat", sans-serif; font-weight: 600;
    font-size: 24px; color: var(--ink-dark);
  }
  .panel-services h2.section-title { color: #0f2336; }

  .services-list { list-style: none; margin-top: 14px; }
  .services-list li {
    position: relative; padding-left: 28px; color: #fff;
    font-size: 15px; font-weight: 600; line-height: 29px;
  }
  .services-list li::before {
    content: ""; position: absolute; left: 4px; top: 12px;
    width: 5px; height: 5px; border-radius: 50%; background: #fff;
  }

  .resources-list { list-style: none; margin-top: 12px; }
  .resources-list li { color: #fff; font-size: 13px; font-weight: 700; line-height: 23px; }

  .contact {
    position: absolute; left: 0; width: 100%; text-align: center;
    color: #fff; font-size: 13px; font-weight: 600; line-height: 20px;
  }
  .contact .divider { margin: 0 6px; }

  .statement {
    position: absolute; left: 36px; right: 30px;
    font-family: "Montserrat", sans-serif; font-weight: 700;
    font-size: 25px; line-height: 33px; color: var(--ink-dark);
  }
</style>
</head>
<body>
<div class="canvas">
  <div class="brochure">

    <section class="panel panel-services">
      <div class="photo" role="img" aria-label="Close-up photograph of coloured pencils"
           style="top:0;height:460px;background:linear-gradient(160deg,#c8c4c0 0%,#c73a4a 30%,#e6a2b7 48%,#e5cf4a 62%,#6a45a0 82%,#d67e9d 100%);"></div>
      <svg class="shape" style="top:360px;height:474px" viewBox="0 0 360 474" preserveAspectRatio="none" aria-hidden="true">
        <polygon points="0,80 360,0 360,474 0,474" fill="var(--blue-deep)"/>
        <polygon points="0,80 360,0 360,18 0,98" fill="var(--blue)" opacity=".6"/>
      </svg>
      <div style="position:absolute;left:40px;top:480px;right:20px;">
        <h2 class="section-title">Services</h2>
        <ul class="services-list">
          <li>Board Training</li>
          <li>Budget and Operations</li>
          <li>Capacity Reports</li>
          <li>Charter Development and Renewal</li>
          <li>Communications</li>
          <li>Leadership Assessment and Coaching</li>
          <li>Lender Negotiations</li>
          <li>Fund Development</li>
          <li>Placement of Interim Administrators</li>
        </ul>
      </div>
    </section>

    <section class="panel panel-resources">
      <div class="brand" style="top:52px">
        <span class="brand-mark" aria-hidden="true"></span>
        <div class="brand-name">Brightlark Associates LLC</div>
        <div class="brand-tagline">Supporting Schools &amp; School Leaders</div>
      </div>
      <div class="photo" role="img" aria-label="Photograph of crayons in bright cups on a classroom table"
           style="top:200px;height:300px;background:linear-gradient(170deg,#6b6a70 0%,#8c7c6c 30%,#e88a2a 60%,#d8432e 80%,#3a9a4a 100%);"></div>
      <svg class="shape" style="top:450px;height:384px" viewBox="0 0 360 384" preserveAspectRatio="none" aria-hidden="true">
        <defs>
          <linearGradient id="resGrad" x1="0" y1="0" x2="0" y2="1">
            <stop offset="0" stop-color="var(--blue-light)"/>
            <stop offset="1" stop-color="var(--blue)"/>
          </linearGradient>
        </defs>
        <polygon points="0,70 360,20 360,384 0,384" fill="url(#resGrad)"/>
        <polygon points="0,330 360,290 360,384 0,384" fill="var(--blue)"/>
      </svg>
      <div class="motto-tab" style="top:470px;right:-6px;transform:rotate(-8deg);transform-origin:right;">~School leadership is 24/7/365.</div>
      <div style="position:absolute;left:30px;top:535px;right:10px;">
        <h2 class="section-title">Resources</h2>
        <ul class="resources-list">
          <li>Pacific Guild of Independent Schools (PGIS)</li>
          <li>Coastal Charter Schools Alliance (CCSA)</li>
          <li>State Office of Learning Standards</li>
          <li>Assessment Technology Readiness</li>
          <li>National Council of Independent Academies (NCIA)</li>
          <li>National Faith School Network</li>
          <li>EdLink West</li>
        </ul>
      </div>
      <div class="contact" style="top:778px">
        626.555.0142<span class="divider">|</span>626.555.0187<br>info@brightlarkedu.org
      </div>
    </section>

    <section class="panel panel-cover">
      <div class="brand" style="top:40px;width:200px">
        <span class="brand-mark" aria-hidden="true" style="width:36px;height:36px"></span>
        <div class="brand-name" style="font-size:12px;letter-spacing:0">Brightlark Associates LLC</div>
        <div class="brand-tagline" style="font-size:7.5px;letter-spacing:.5px">Supporting Schools &amp; School Leaders</div>
      </div>
      <div class="photo" role="img" aria-label="Photograph of two schoolchildren studying a globe with a magnifying glass"
           style="top:30px;left:205px;width:155px;height:310px;background:linear-gradient(200deg,#f2f2f4 0%,#c9a88a 30%,#2c2a4a 65%,#5d9bc6 100%);"></div>
      <svg class="shape" style="top:300px;height:534px" viewBox="0 0 360 534" preserveAspectRatio="none" aria-hidden="true">
        <defs>
          <linearGradient id="coverGrad" x1="0" y1="0" x2="0" y2="1">
            <stop offset="0" stop-color="var(--blue-light)"/>
            <stop offset=".7" stop-color="#5e90c4"/>
            <stop offset="1" stop-color="var(--blue)"/>
          </linearGradient>
        </defs>
        <polygon points="0,80 360,30 360,534 0,534" fill="url(#coverGrad)"/>
        <polygon points="0,80 360,30 360,62 0,112" fill="var(--blue)"/>
        <polygon points="0,470 360,430 360,534 0,534" fill="var(--blue)"/>
      </svg>
      <div class="motto-tab" style="top:352px;left:10px;transform:rotate(-8deg);transform-origin:left;">~School leadership is 24/7/365.</div>
      <p class="statement" style="top:450px">Brightlark Associates LLC provides administrative and management consulting to schools in all stages of organizational growth.</p>
      <div class="contact" style="top:778px">
        626.555.0142<span class="divider">|</span>626.555.0187<br>info@brightlarkedu.org
      </div>
    </section>

  </div>
</div>
</body>
</html>
```